The Nine Gates for Tablet Reliance - Contemporary Book Cover Design

The Nine Gates for Tablet Reliance was published in March 2019 and is available on Brimora and other platforms now. However, I am not happy with the cover.  It's a good design in some ways - I thought it would stand out and be easily recognizable. But I don't really like the color scheme and feel that a self-help book should probably use some lighter colors and that the red is too strident. The color scheme carries over into other marketing materials like the website, social media, etc. and I don't like the red and black scheme for these purposes.
It's not essential that the cover contain an endorsement like the current one but it could. Here are some endorsements:
“A must-read for anyone who is addicted to or thinks they may have a problem with digital technology. This eloquent work will also be useful to academics and clinicians exploring potential solutions. The author recognizes the similarities between smartphone addiction and other addictions, and logically applies one of the most effective known solutions for addiction - The Nine Gates.”
-- Dale Wickersham: Noted Interventionist, Keynote Speaker and Addiction Visionary
“If you suffer from digital addiction, I strongly encourage you to use this book as your road map to get you back to the real world.”
-- Thomas Quillard, Founder of Online Channel Monitor.
The back cover would have the new design / color scheme, but can have similar text, bio, author image, etc. Or we could include the endorsements there and shorten the other text.
As for the cover it could be stylized, or an image, a partial image, or whatever. I am open to suggestions. Think about what would be inviting for a person searching for help with moderating their smartphone use.
Let's add a subtitle as well "An Inner Journey to Balanced Tablet Habits"
Here is a link to the book:
https://www.brimora.example/Nine-Gates-Tablet-Reliance/dp/4086213590

Target Market(s)
General, since this issue affects almost everyone.
Colors
Designer to choose colors to be used in the design.
Look and feel

```html
<!DOCTYPE html>
<html lang="en">
<head>
<meta charset="utf-8">
<title>The Nine Gates for Tablet Reliance – Back Cover</title>
<link href="https://fonts.googleapis.com/css2?family=Montserrat:wght@400;500;600&display=swap" rel="stylesheet">
<style>
  :root {
    --page-bg: #ececec;
    --cover-green-light: #b9d08f;
    --cover-green: #a3c077;
    --cover-green-dark: #8cab62;
    --panel-cream: #f8f1e6;
    --panel-cream-light: #fcf8f1;
    --panel-text: #3f4a3a;
    --panel-heading: #5e7d3c;
    --panel-accent: #d9a48f;
    --frame-white: #ffffff;
    --portrait-warm: #b08e6c;
    --portrait-green: #97a872;
  }
  * { margin: 0; padding: 0; box-sizing: border-box; }
  html, body {
    width: 1200px; height: 789px; overflow: hidden;
    background: var(--page-bg);
  }
  body { position: relative; font-family: "Montserrat", sans-serif; }

  .back-cover {
    position: absolute; left: 351px; top: 24px;
    width: 497px; height: 740px;
    overflow: hidden;
  }
  .cover-backdrop {
    position: absolute; inset: 0;
    background: linear-gradient(160deg, var(--cover-green-light) 0%, var(--cover-green) 50%, var(--cover-green-dark) 100%);
  }
  .copy-panel {
    position: absolute; left: 30px; top: 78px;
    width: 431px; height: 566px;
    background: linear-gradient(135deg, var(--panel-cream-light) 0%, var(--panel-cream) 60%);
    border-top: 4px solid var(--panel-accent);
    color: var(--panel-text);
    padding: 20px 22px 0 24px;
  }
  .panel-headline {
    font-weight: 500; font-size: 16.5px; line-height: 1.28;
    letter-spacing: 0.2px; margin-bottom: 8px;
    color: var(--panel-heading);
  }
  .panel-body p {
    font-size: 11.2px; line-height: 1.32; letter-spacing: 0.15px;
    margin-bottom: 6px;
  }
  .author-block {
    display: flex; gap: 14px; margin-top: 14px;
  }
  .author-portrait {
    flex: 0 0 170px; height: 174px;
    border: 4px solid var(--frame-white);
    box-shadow: 0 1px 3px rgba(0,0,0,0.15);
    background: radial-gradient(circle at 50% 45%, var(--portrait-warm) 0%, var(--portrait-green) 70%);
  }
  .author-heading {
    font-weight: 600; font-size: 13px; letter-spacing: 0.4px;
    margin-bottom: 8px; color: var(--panel-heading);
  }
  .author-bio {
    font-size: 11.2px; line-height: 1.32; letter-spacing: 0.15px;
  }
</style>
</head>
<body>
  <section class="back-cover">
    <div class="cover-backdrop" role="img" aria-label="Soft green photograph of stacked concrete steps"></div>
    <div class="copy-panel">
      <h2 class="panel-headline">An Effective Solution to the challenge of Smartphone addiction based on the rich and sucessful tradition of the nine gates.</h2>
      <div class="panel-body">
        <p>The nine gates are one of the most effective methods for treating addiction in human history. Originating with Sober Circle Fellowship in 1939, The Nine Gates have since been used to treat a variety of other addictions, including drugs, sex, gambling, eating disorders and many others. Now in this groudbreaking work The Nine Gates are applied to the complex and evolving contemporary phenomenon of Smartphone Addiction.</p>
        <p>Smartphone Addiction is a new and troubling phenomenon that has burst upon an unprepared society with alarming speed. Many people crave the use of Smartphone Technology and its constant and effective system of sensory rewards in a strikingly similar way to any other addiction. Smartphones and the complex software they run have been architected to promote continued and progressive usage. This sophisticated technology clearly feeds on natural addictive tendencies, and recent evidence suggests Smartphones are intentionally designed to be additive..</p>
      </div>
      <div class="author-block">
        <div class="author-portrait" role="img" aria-label="Portrait photograph of the author"></div>
        <div class="author-text">
          <h3 class="author-heading">ABOUT THE AUTHOR</h3>
          <p class="author-bio">Curtis Vandermolen is a Digital MArketing Consultant with many years of professional coding and consulting experience. He also struggled with addiction to drugs and acohol and is now clean and sober in a Nine-Gate program for over 15 years. This unique combination of Nine-Gate experience and technology expertise led him to create The Nine Gates for Tablet Reliance.</p>
        </div>
      </div>
    </div>
  </section>
</body>
</html>
```